Health and Wellness company needs flyer to promote free seminar

Stride reform studio is a health and wellness company that offers an exercise program designed by physical therapists to help relieve pain and improve mobility. Our business is a new concept that is not well understood by the public. In order to promote our business we offer a free seminar where we present information regarding the underlying cause of pain and tightness. During the seminar we also perform a posture screen and movement testing for all participants.

Target Market(s)

Mostly healthy and active women ages 25-65

Industry/Entity Type

Health And Wellness

Font styles to use
Sans Serif

Colors

Designer to choose colors to be used in the design.

Requirements
Must have
• Title: Eliminate Pain and Tightness For Good
• Paragraph: Stride Reform Studio offers a free 60 minute seminar: "The Busy Walker's Handbook to Bending and Standing Taller."
• What to Expect:
• • Identify the underlying cause of your pain and mobility issues
• • Expose what gets in the way of you moving and feeling better
• • Learn why traditional exercises don’t help and can actually make the problem worse
• • Reveal what your posture is saying and how that impacts you
• • Experience your muscle imbalances through movement tests
• • Discover the training method that realigns your posture, increases your mobility and reduces your pain
• Call to action: RSVP online at stridereformstudio.com
Nice to have
• Use a relevant image showing a female dealing with tightness in the low back, legs, etc.
• Emphasize that the seminar is FREE.
• Make the call to action prominent.

```html
<!DOCTYPE html>
<html lang="en">
<head>
<meta charset="utf-8">
<title>Stride Reform Studio – Free Seminar Flyer</title>
<link href="https://fonts.googleapis.com/css2?family=Questrial&family=Lato:wght@400;700&display=swap" rel="stylesheet">
<style>
  :root {
    --canvas: #e6e6e6;
    --paper: #ffffff;
    --orange: #f39322;
    --purple: #5558a8;
    --purple-dark: #414685;
    --ink: #2b2b2b;
    --white: #ffffff;
  }
  * { box-sizing: border-box; margin: 0; padding: 0; }
  html, body { width: 1200px; height: 1200px; overflow: hidden; background: var(--canvas); }
  .flyer {
    position: absolute; left: 194px; top: 30px;
    width: 812px; height: 1140px;
    background: var(--paper); overflow: hidden;
    box-shadow: 0 4px 16px rgba(0,0,0,.25);
  }
  .title-band {
    position: absolute; left: 0; top: 0; width: 208px; height: 1002px;
    background: var(--orange); overflow: hidden;
  }
  .title-brackets { position: absolute; left: 0; top: 0; }
  .headline {
    position: absolute; left: -395px; top: 395px; width: 1000px; height: 200px;
    transform: rotate(-90deg);
    display: flex; flex-direction: column; justify-content: center; align-items: center;
    font-family: "Questrial", sans-serif; color: var(--white);
    font-size: 62px; line-height: 76px; white-space: nowrap;
  }
  .headline .emphasis { font-size: 64px; letter-spacing: 1px; }
  .hero-photo {
    position: absolute; left: 208px; top: 0; width: 604px; height: 520px;
    background:
      linear-gradient(to bottom, rgba(255,255,255,0) 78%, #ffffff 100%),
      linear-gradient(to bottom, #8a8091 0%, #e0a86a 18%, #f5c15a 30%, #b7a1a6 40%, #9c8e9c 55%, #c7a04e 70%, #d6ac5a 85%, #efe4d0 100%);
  }
  .intro {
    position: absolute; left: 229px; top: 518px; width: 560px;
    font-family: "Questrial", sans-serif;
  }
  .intro .lead { font-size: 25px; color: var(--ink); font-weight: 700; }
  .intro .offer { font-size: 38px; color: var(--purple); margin-top: 4px; font-weight: 700; }
  .intro .offer .colon { color: var(--ink); }
  .intro .seminar-name { font-size: 29px; color: var(--orange); line-height: 36px; margin-top: 8px; font-weight: 700; }
  .expect {
    position: absolute; left: 233px; top: 694px; width: 560px;
    font-family: "Lato", sans-serif; color: var(--ink);
  }
  .expect h2 { font-size: 21px; font-weight: 700; text-decoration: underline; text-underline-offset: 3px; margin-bottom: 14px; }
  .expect ul { list-style: none; }
  .expect li { position: relative; padding-left: 24px; font-size: 17px; line-height: 22px; margin-bottom: 11px; }
  .expect li svg { position: absolute; left: 1px; top: 3px; }
  .cta-band {
    position: absolute; left: 0; top: 1002px; width: 812px; height: 138px;
    background: linear-gradient(90deg, var(--purple-dark), var(--purple) 50%, var(--purple-dark));
    color: var(--white); font-family: "Lato", sans-serif;
  }
  .cta-text { position: absolute; left: 42px; top: 42px; font-size: 21px; line-height: 27px; }
  .cta-text strong { font-weight: 700; }
  .brand { position: absolute; right: 40px; top: 46px; display: flex; align-items: center; gap: 10px; font-size: 25px; }
  .brand .mark { width: 40px; height: 40px; border: 3px solid var(--white); }
</style>
</head>
<body>
<main class="flyer">
  <section class="title-band">
    <svg class="title-brackets" width="208" height="1002" aria-hidden="true">
      <path d="M30 69 V43 H175 V69" fill="none" stroke="#fff" stroke-width="5"/>
      <path d="M30 930 V956 H175 V930" fill="none" stroke="#fff" stroke-width="5"/>
    </svg>
    <h1 class="headline">
      <span>Eliminate Pain and Tightness</span>
      <span class="emphasis">FOR GOOD</span>
    </h1>
  </section>

  <div class="hero-photo" role="img" aria-label="Woman with arms outstretched in tall golden grass facing a sunset over the sea"></div>

  <section class="intro">
    <p class="lead">Stride Reform Studio offers a</p>
    <p class="offer">Free 60 minute seminar<span class="colon">:</span></p>
    <p class="seminar-name">"The Busy Walker's Handbook to Bending and Standing Taller."</p>
  </section>

  <section class="expect">
    <h2>What to Expect:</h2>
    <ul>
      <li><svg width="18" height="16" aria-hidden="true"><rect x="1" y="3" width="12" height="12" fill="none" stroke="#5558a8" stroke-width="1.6"/><path d="M4 9 L7 12 L16 1" fill="none" stroke="#5558a8" stroke-width="2"/></svg>Identify the underlying cause of your pain and mobility issues</li>
      <li><svg width="18" height="16" aria-hidden="true"><rect x="1" y="3" width="12" height="12" fill="none" stroke="#5558a8" stroke-width="1.6"/><path d="M4 9 L7 12 L16 1" fill="none" stroke="#5558a8" stroke-width="2"/></svg>Expose what gets in the way of you moving and feeling better</li>
      <li><svg width="18" height="16" aria-hidden="true"><rect x="1" y="3" width="12" height="12" fill="none" stroke="#5558a8" stroke-width="1.6"/><path d="M4 9 L7 12 L16 1" fill="none" stroke="#5558a8" stroke-width="2"/></svg>Learn why traditional exercises don’t help and can actually make the problem worse</li>
      <li><svg width="18" height="16" aria-hidden="true"><rect x="1" y="3" width="12" height="12" fill="none" stroke="#5558a8" stroke-width="1.6"/><path d="M4 9 L7 12 L16 1" fill="none" stroke="#5558a8" stroke-width="2"/></svg>Reveal what your posture is saying and how that impacts you</li>
      <li><svg width="18" height="16" aria-hidden="true"><rect x="1" y="3" width="12" height="12" fill="none" stroke="#5558a8" stroke-width="1.6"/><path d="M4 9 L7 12 L16 1" fill="none" stroke="#5558a8" stroke-width="2"/></svg>Experience your muscle imbalances through movement tests</li>
      <li><svg width="18" height="16" aria-hidden="true"><rect x="1" y="3" width="12" height="12" fill="none" stroke="#5558a8" stroke-width="1.6"/><path d="M4 9 L7 12 L16 1" fill="none" stroke="#5558a8" stroke-width="2"/></svg>Discover the training method that realigns your posture, increases your mobility and reduces your pain</li>
    </ul>
  </section>

  <footer class="cta-band">
    <p class="cta-text">Sign up online at<br><strong>stridereformstudio.com/free-seminar</strong></p>
    <div class="brand"><span class="mark"></span><span>stridereformstudio</span></div>
  </footer>
</main>
</body>
</html>
```